Bramblecourt Homes Stationary
Fast Settlements
Professional
Dorian Pelletier
Managing Member
4817 Larkspur Ave Suite 210
Washington, DC
dgpelletier@bramblecourthomes.net
www.bramblecourthomes.net
Business License # 782645113058
Cash Buyer, Fast Closing.
Residential and Commercial
We are a Nation Wide Buyer.
will upload ai file shortly
vector logo file

```html
<!DOCTYPE html>
<html lang="en">
<head>
<meta charset="utf-8">
<title>Bramblecourt Homes – Business Card</title>
<link rel="stylesheet" href="https://fonts.googleapis.com/css2?family=Michroma&display=swap">
<style>
  :root {
    --backdrop: #e6e4e0;
    --card: #ffffff;
    --brand-green: #1f8a3c;
    --brand-green-dark: #15692c;
    --ink: #4a4a4a;
    --ink-soft: #7a7a7a;
    --band: #3a3a3a;
  }
  * { margin: 0; padding: 0; box-sizing: border-box; }
  html, body {
    width: 1200px; height: 902px; overflow: hidden;
    background: var(--backdrop);
    font-family: "Michroma", sans-serif;
  }
  .business-card {
    position: absolute; left: 100px; top: 165px;
    width: 1000px; height: 572px;
    background: var(--card);
    border-radius: 6px;
    box-shadow: 0 10px 30px rgba(0,0,0,.18);
    overflow: hidden;
  }
  .brand {
    position: absolute; top: 110px; left: 0; width: 100%;
    display: flex; justify-content: center; align-items: center; gap: 18px;
  }
  .brand-mark { width: 30px; height: 30px; background: var(--brand-green); flex: none; }
  .brand-name { font-size: 44px; line-height: 1.2; color: var(--brand-green); letter-spacing: 1px; white-space: nowrap; }
  .brand-rule {
    position: absolute; top: 196px; left: 330px; width: 340px;
    border-top: 2px dotted var(--ink-soft);
  }
  .person { position: absolute; top: 224px; left: 0; width: 100%; text-align: center; }
  .person-name { font-size: 15px; color: var(--brand-green); letter-spacing: 1px; }
  .person-title { font-size: 13px; color: var(--ink); margin-top: 8px; letter-spacing: 1px; }
  .contact-row {
    position: absolute; top: 318px; left: 40px; right: 40px;
    display: flex; justify-content: space-between; align-items: center;
    font-size: 13px; color: var(--ink); letter-spacing: .3px; white-space: nowrap;
  }
  .contact-line-two {
    position: absolute; top: 356px; left: 40px; right: 40px;
    display: flex; justify-content: space-between; align-items: center;
    font-size: 13px; color: var(--ink); letter-spacing: .3px; white-space: nowrap;
  }
  .contact-item { display: flex; align-items: center; }
  .icon { width: 17px; height: 17px; margin-right: 7px; flex: none; }
  .bottom-band {
    position: absolute; left: 0; right: 0; bottom: 0; height: 62px;
    background: var(--band);
  }
  .url-tab {
    position: absolute; left: 200px; right: 200px; bottom: 0; height: 88px;
    background: linear-gradient(var(--brand-green), var(--brand-green-dark));
    border-radius: 12px 12px 0 0;
    display: flex; align-items: center; justify-content: center;
    color: #fff; font-size: 26px; letter-spacing: 2px; white-space: nowrap;
  }
</style>
</head>
<body>
  <div class="business-card">
    <div class="brand">
      <span class="brand-mark"></span>
      <span class="brand-name">Bramblecourt Homes</span>
    </div>
    <div class="brand-rule"></div>

    <div class="person">
      <div class="person-name">Dorian Pelletier</div>
      <div class="person-title">Managing Member</div>
    </div>

    <div class="contact-row">
      <span class="contact-item">
        <svg class="icon" viewBox="0 0 20 20"><circle cx="10" cy="10" r="10" fill="#1f8a3c"/><path d="M7 5l2 3-1.2 1.2a7 7 0 0 0 3 3L12 11l3 2-1 2c-4 0-8-4-8-8z" fill="#fff"/></svg>
        1-800-555-0147
      </span>
      <span class="contact-item">
        <svg class="icon" viewBox="0 0 20 20"><circle cx="10" cy="10" r="10" fill="#1f8a3c"/><path d="M7 5l2 3-1.2 1.2a7 7 0 0 0 3 3L12 11l3 2-1 2c-4 0-8-4-8-8z" fill="#fff"/></svg>
        202-555-0183
      </span>
      <span class="contact-item">
        <svg class="icon" viewBox="0 0 20 20"><circle cx="10" cy="10" r="10" fill="#1f8a3c"/><path d="M7 5l2 3-1.2 1.2a7 7 0 0 0 3 3L12 11l3 2-1 2c-4 0-8-4-8-8z" fill="#fff"/></svg>
        410-555-0129
      </span>
      <span class="contact-item">
        <svg class="icon" viewBox="0 0 20 20"><circle cx="10" cy="10" r="10" fill="#1f8a3c"/><rect x="5" y="6.5" width="10" height="7" fill="none" stroke="#fff" stroke-width="1.4"/><path d="M5 6.5l5 4 5-4" fill="none" stroke="#fff" stroke-width="1.4"/></svg>
        dgpelletier@bramblecourthomes.net
      </span>
    </div>

    <div class="contact-line-two">
      <span class="contact-item">
        <svg class="icon" viewBox="0 0 20 20"><circle cx="10" cy="10" r="10" fill="#1f8a3c"/><path d="M10 4a4 4 0 0 0-4 4c0 3 4 8 4 8s4-5 4-8a4 4 0 0 0-4-4z" fill="#fff"/><circle cx="10" cy="8" r="1.5" fill="#1f8a3c"/></svg>
        4817 Larkspur Ave Suite 210 Fairhaven, MD 20779
      </span>
      <span class="contact-item">
        <svg class="icon" viewBox="0 0 20 20"><circle cx="10" cy="10" r="10" fill="#1f8a3c"/><circle cx="10" cy="10" r="5" fill="none" stroke="#fff" stroke-width="1.3"/><path d="M5 10h10M10 5v10" stroke="#fff" stroke-width="1.1"/></svg>
        www.bramblecourthomes.net
      </span>
    </div>

    <div class="bottom-band"></div>
    <div class="url-tab">www.BramblecourtHomes.net</div>
  </div>
</body>
</html>
```